Modern Banner for use on Emails and Electronic letters.

We need a Email banner that we can also uses as a banner on electronic documents . Would be a bonus to be able to use banner on chatterloop.
The banner should incorporate our logo and company name; The OnaVelt Group.
We would like an eye catching, modern design.
We are completely open to using colour and/or images along with our logo and company name.
Currently the font for our company name is time new roman but again we are open to suggestions. The company name can be be moved away from the umbrella logo to anywhere in the banner.

Industry/Entity Type

Electronic

Font styles to use
Serif
Sans Serif

Colors

Designer to choose colors to be used in the design.

Requirements
Must have
• OnaVelt Logo (Umbrella design - Black umbrella on red blocks with a letter on each block spelling VELT.
• Company name: The OnaVelt Group
• Be Modern and professional.
• Suitable for use as an email banner but can also be used as letterhead on electronic documents.
Nice to have
• Colour and/or images.
• Be able to be used as chatterloop banner.

```html
<!DOCTYPE html>
<html lang="en">
<head>
<meta charset="utf-8">
<title>The OnaVelt Group – Letterhead</title>
<link rel="stylesheet" href="https://fonts.googleapis.com/css2?family=Tinos:wght@400&display=swap">
<style>
  :root {
    --page: #ffffff;
    --band-dark: #0a0a0a;
    --band-mid: #3a3d3d;
    --band-light: #a9adab;
    --brand-red: #d8120c;
    --brand-red-deep: #8e0c08;
    --ink: #151515;
    --title: #ffffff;
  }
  html, body {
    margin: 0;
    padding: 0;
    width: 856px;
    height: 1200px;
    overflow: hidden;
    background: var(--page);
  }
  .letterhead {
    position: relative;
    width: 856px;
    height: 1200px;
    background: var(--page);
    font-family: "Tinos", "Times New Roman", serif;
  }
  .banner {
    position: absolute;
    left: 0;
    top: 0;
    width: 702px;
    height: 112px;
    background:
      radial-gradient(ellipse 200px 160px at 380px 56px, var(--band-light) 0%, var(--band-mid) 40%, rgba(20,20,20,0) 100%),
      linear-gradient(90deg,
        var(--brand-red) 0%, var(--brand-red-deep) 9%, var(--band-dark) 17%,
        #1c1c1c 35%, #1c1c1c 65%,
        var(--band-dark) 82%, var(--brand-red-deep) 90%, var(--brand-red) 100%);
    overflow: hidden;
  }
  .company-title {
    position: absolute;
    left: 0;
    width: 756px;
    top: 30px;
    margin: 0;
    text-align: center;
    color: var(--title);
    font-weight: 400;
    white-space: nowrap;
    text-shadow: 1px 1px 1px rgba(0,0,0,0.6);
  }
  .company-title .small { font-size: 28px; }
  .company-title .large { font-size: 48px; }
  .brand-mark {
    position: absolute;
    left: 724px;
    top: 0;
    width: 132px;
    height: 112px;
    display: flex;
    flex-direction: column;
    align-items: center;
    justify-content: center;
    gap: 8px;
    color: var(--ink);
    font-size: 30px;
    font-weight: 400;
  }
  .brand-mark .square {
    width: 22px;
    height: 22px;
    background: var(--brand-red);
  }
  .corner-block {
    position: absolute;
    left: 818px;
    top: 1166px;
    width: 32px;
    height: 30px;
    background: var(--brand-red);
  }
</style>
</head>
<body>
  <div class="letterhead">
    <header class="banner" role="img" aria-label="Dark gradient banner with scattered red cubes">
      <h1 class="company-title"><span class="small">The </span><span class="large">OnaVelt</span><span class="small"> Group</span></h1>
    </header>
    <div class="brand-mark"><span class="square"></span>OnaVelt</div>
    <div class="corner-block" aria-hidden="true"></div>
  </div>
</body>
</html>
```